New Business Card Design Project

We are looking for a talented individual to create a truly awesome/unique business card design for us. We are looking for a someone to design something that will really stand out from the crowd - we don't mind what ideas you come up with (ie embossed/flat/matte/shine etc etc) just wow us with your creativity.
Updates

Target Market(s)

Video Games Industry Professionals (all levels of seniority from QA Testers through to CEOs)

Contact Information for Business Card

Company logo (see upload)
Company name: Northbay Play Careers Ltd
Employee Name: Darren Elsby
Job title: CEO
Website: www.nbpc2go.example
Office +44 1632 960418
Mobile: +44 7700 900276
Email: darren@nbpc2go.example

Colors

Designer to choose colors to be used in the design.

Requirements
Must have
• The business card design MUST contain all the information listed in the BUSINESS CARD DETAILS box.
• You will see the colours that are relevant to us (ie company logo) in the uploaded imagery - however you do not have to use all these colours when designing the business card itself
• MUST BE DOUBLE SIDED

```html
<!DOCTYPE html>
<html lang="en">
<head>
<meta charset="utf-8">
<title>Northbay Play Careers – Business Card</title>
<link href="https://fonts.googleapis.com/css2?family=Open+Sans:wght@400;600;700&display=swap" rel="stylesheet">
<style>
  :root {
    --bg: #f2eeee;
    --card: #ffffff;
    --charcoal: #2e2e2f;
    --charcoal-soft: #3d3d3f;
    --amber: #f4b633;
    --orange: #f07a14;
    --navy: #1f2b5e;
    --ink: #3a3a3a;
    --ink-soft: #555555;
    --rule: #6b6b6b;
  }
  * { margin: 0; padding: 0; box-sizing: border-box; }
  html, body { width: 1200px; height: 630px; overflow: hidden; }
  body {
    background: var(--bg);
    font-family: "Open Sans", Arial, sans-serif;
    display: flex;
    align-items: center;
    justify-content: center;
    gap: 40px;
  }
  .card {
    position: relative;
    width: 540px;
    height: 302px;
    background: var(--card);
    border-radius: 16px;
    overflow: hidden;
    box-shadow: 0 10px 22px rgba(0,0,0,0.28);
  }
  .card-shapes { position: absolute; inset: 0; width: 100%; height: 100%; }

  /* Front */
  .front-brand {
    position: absolute;
    left: 0; right: 0; top: 98px;
    display: flex;
    flex-direction: column;
    align-items: center;
  }
  .brand-row { display: flex; align-items: center; gap: 10px; }
  .brand-dot {
    width: 34px; height: 34px; border-radius: 50%;
    background: var(--navy);
  }
  .brand-name {
    font-weight: 700;
    font-size: 23px;
    color: var(--navy);
    letter-spacing: -0.2px;
  }
  .brand-rule {
    width: 290px; height: 1.5px;
    background: var(--ink);
    margin-top: 10px;
  }
  .company-legal {
    margin-top: 4px;
    font-size: 15.5px;
    color: var(--ink);
    letter-spacing: 0.2px;
  }

  /* Back */
  .back-brand {
    position: absolute;
    right: 24px; top: 50px;
    display: flex; align-items: center; gap: 8px;
  }
  .back-brand .brand-dot { width: 26px; height: 26px; background: #ffffff; }
  .back-brand .brand-name { font-size: 15px; color: #ffffff; }

  .holder { position: absolute; left: 32px; top: 36px; }
  .holder-name {
    font-size: 23px;
    font-weight: 600;
    letter-spacing: 0.6px;
    color: var(--charcoal);
    text-transform: uppercase;
    line-height: 1;
  }
  .holder-name .surname { color: var(--orange); }
  .holder-rule {
    position: relative;
    width: 166px; height: 1.5px;
    background: var(--rule);
    margin-top: 5px;
  }
  .holder-rule::before {
    content: ""; position: absolute; left: 0; top: -0.5px;
    width: 20px; height: 2.5px; background: var(--orange);
  }
  .holder-role {
    margin-top: 3px; margin-left: 14px;
    font-size: 8px; color: var(--ink-soft);
  }

  .contact-list {
    position: absolute; left: 30px; top: 140px;
    list-style: none;
  }
  .contact-item {
    display: flex; align-items: center; gap: 12px;
    height: 34px; margin-bottom: 12px;
  }
  .contact-icon {
    width: 34px; height: 34px; border-radius: 50%;
    background: var(--amber);
    display: flex; align-items: center; justify-content: center;
    flex-shrink: 0;
  }
  .contact-icon svg { width: 18px; height: 18px; }
  .contact-text { font-size: 10px; color: var(--ink); line-height: 1.4; }
</style>
</head>
<body>

  <!-- Front side -->
  <section class="card card-front" aria-label="Business card front">
    <svg class="card-shapes" viewBox="0 0 500 280" preserveAspectRatio="none" aria-hidden="true">
      <path d="M0 0 H330 C285 6 255 36 205 38 H0 Z" fill="var(--charcoal)"/>
      <path d="M205 38 C255 36 285 6 330 0 H500 V26 C450 24 420 30 380 34 C330 38 270 40 205 40 Z" fill="var(--amber)"/>
      <path d="M0 0 H140 L60 38 H0 Z" fill="#ffffff" opacity="0.05"/>
      <path d="M0 240 H250 C290 240 310 256 330 280 H0 Z" fill="var(--amber)"/>
      <path d="M245 280 C275 262 300 246 345 244 H500 V280 Z" fill="var(--charcoal)"/>
      <path d="M240 280 C272 260 300 242 345 240 H500 V244 H345 C300 246 275 262 245 280 Z" fill="#ffffff"/>
      <path d="M380 280 L450 244 H500 V280 Z" fill="#ffffff" opacity="0.05"/>
    </svg>
    <div class="front-brand">
      <div class="brand-row">
        <span class="brand-dot"></span>
        <span class="brand-name">Northbay Play Careers</span>
      </div>
      <div class="brand-rule"></div>
      <p class="company-legal">Northbay Play Careers Ltd</p>
    </div>
  </section>

  <!-- Back side -->
  <section class="card card-back" aria-label="Business card back">
    <svg class="card-shapes" viewBox="0 0 500 280" preserveAspectRatio="none" aria-hidden="true">
      <path d="M272 0 H500 V280 H302 C292 240 296 190 288 165 C280 140 272 130 272 110 Z" fill="var(--charcoal)"/>
      <path d="M330 0 L500 120 V0 Z" fill="#ffffff" opacity="0.04"/>
      <path d="M300 280 L420 150 L500 230 V280 Z" fill="#ffffff" opacity="0.04"/>
      <path d="M280 150 C266 190 268 240 276 280 H296 C290 240 292 195 280 150 Z" fill="var(--amber)"/>
      <path d="M276 280 C268 240 266 190 280 150 L278 150 C263 190 265 240 272 280 Z" fill="#ffffff"/>
    </svg>

    <div class="back-brand">
      <span class="brand-dot"></span>
      <span class="brand-name">Northbay Play Careers</span>
    </div>

    <div class="holder">
      <h1 class="holder-name">Darren <span class="surname">Elsby</span></h1>
      <div class="holder-rule"></div>
      <p class="holder-role">CEO</p>
    </div>

    <ul class="contact-list">
      <li class="contact-item">
        <span class="contact-icon">
          <svg viewBox="0 0 24 24" fill="none" stroke="#ffffff" stroke-width="2" stroke-linejoin="round">
            <rect x="3" y="6" width="18" height="12" rx="1"/>
            <path d="M3 7 L12 13 L21 7"/>
          </svg>
        </span>
        <span class="contact-text">darren@nbpc2go.example</span>
      </li>
      <li class="contact-item">
        <span class="contact-icon">
          <svg viewBox="0 0 24 24" fill="none" stroke="#ffffff" stroke-width="2" stroke-linecap="round" stroke-linejoin="round">
            <path d="M5 4 H9 L11 9 L8.5 10.5 A11 11 0 0 0 13.5 15.5 L15 13 L20 15 V19 A2 2 0 0 1 18 21 A16 16 0 0 1 3 6 A2 2 0 0 1 5 4 Z"/>
          </svg>
        </span>
        <span class="contact-text">+44 1632 960418<br>+44 7700 900276</span>
      </li>
      <li class="contact-item">
        <span class="contact-icon">
          <svg viewBox="0 0 24 24" fill="none" stroke="#ffffff" stroke-width="1.8">
            <circle cx="12" cy="12" r="9"/>
            <ellipse cx="12" cy="12" rx="4" ry="9"/>
            <path d="M3 12 H21 M5 7 H19 M5 17 H19"/>
          </svg>
        </span>
        <span class="contact-text">www.nbpc2go.example</span>
      </li>
    </ul>
  </section>

</body>
</html>
```